Welcome Booklet for Plastic Surgery Patients

I need a welcome booklet for a plastic surgery office. We already have the content and a logo, we just need help putting together a design for the booklet. The book details the types of procedures offered by the doctor (Loriane Whitcombe M.D). Attached is a booklet from another doctor as a reference point (Varnholt Plastic Surgery).
We would like it to be mainly white, gray, black with a little bit of pink as a reflection of the doctors work with Breast Cancer.

Target Market(s)

It is meant to be informative for women seeking Breast Reconstruction who have been diagnosed with breast cancer.

Industry/Entity Type

Plastic

Font styles to use
Other font styles liked:
• century gothic

Colors
7f7f7f
ffffff
1b1b1b
eda3c7

Requirements
Must have
• - Address shown on the back page (we have two locations) -
• 218 S Wexmoor Suite 306 Beverly Hills CA 90211
• 17842 Pellham Street Suite 209 Torrance CA 90503
• - The personal picture of Dr. Whitcombe needs to be on the welcome page
• - Pages 3-7 should have breast reconstruction at the top
• - Page 8 should have face at the top
• - Page 9 Should have body at the top
• - Attached is the image we want for the cover
Nice to have
• -The names of the procedures to stand out
• - For the most part we want a very clean look
• - The logo has been uploaded if there is a good place to place it

```html
<!DOCTYPE html>
<html lang="en">
<head>
<meta charset="UTF-8">
<title>Welcome Booklet – Pages 7 &amp; 8</title>
<link rel="stylesheet" href="https://fonts.googleapis.com/css2?family=Questrial&display=swap">
<style>
  :root {
    --backdrop: #e4e4e6;
    --paper: #ffffff;
    --charcoal: #3d3d3e;
    --ink: #1b1b1b;
    --grey: #7f7f7f;
    --pink: #eda3c7;
    --light-text: #ececec;
  }
  * { box-sizing: border-box; margin: 0; padding: 0; }
  html, body { width: 1200px; height: 926px; overflow: hidden; }
  body {
    background: var(--backdrop);
    font-family: "Questrial", "Century Gothic", sans-serif;
    position: relative;
  }
  .spread {
    position: absolute;
    left: 40px; top: 183px;
    width: 1120px; height: 560px;
    display: flex;
    box-shadow: 0 12px 30px rgba(0,0,0,0.18);
  }
  .page { position: relative; width: 560px; height: 560px; overflow: hidden; background: var(--paper); }
  .page--left::after, .page--right::before {
    content: ""; position: absolute; top: 0; bottom: 0; width: 24px; pointer-events: none;
  }
  .page--left::after { right: 0; background: linear-gradient(to left, rgba(0,0,0,0.10), transparent); }
  .page--right::before { left: 0; background: linear-gradient(to right, rgba(0,0,0,0.10), transparent); z-index: 2; }

  /* Left page */
  .cost-panel {
    position: absolute; left: 0; top: 0; bottom: 0; width: 236px;
    background: var(--charcoal);
    padding: 46px 22px 0 24px;
    color: var(--light-text);
  }
  .section-title {
    color: var(--pink);
    font-weight: 400;
    font-size: 23px;
    line-height: 1.08;
    margin-bottom: 14px;
    letter-spacing: 0.3px;
  }
  .body-copy { font-size: 10px; line-height: 1.42; margin-bottom: 14px; }
  .ribbon-mark {
    position: absolute; left: 24px; bottom: 24px;
    width: 10px; height: 16px; background: var(--pink); border-radius: 2px;
  }
  .ribbon-visual {
    position: absolute; left: 268px; top: 40px; width: 250px; height: 380px;
    background: radial-gradient(ellipse at 50% 45%, #f2b6d3 0%, #eba7c8 45%, #f6e4ed 75%, var(--paper) 100%);
  }
  .web-address {
    position: absolute; left: 270px; right: 30px; bottom: 50px;
    font-size: 10px; color: var(--grey); text-align: right;
    letter-spacing: 0.4px;
    padding-bottom: 6px;
    border-bottom: 1px solid #cfcfcf;
  }

  /* Right page */
  .portrait {
    position: absolute; left: 0; top: 0; width: 270px; height: 330px;
    background: linear-gradient(160deg, #8a6a52 0%, #d9ab8c 35%, #e8c2a6 60%, #f1dccb 100%);
  }
  .facelift {
    position: absolute; left: 292px; top: 42px; width: 240px;
    color: var(--grey);
  }
  .facelift .section-title { font-size: 20px; margin-bottom: 6px; }
  .facelift .body-copy { font-size: 9.5px; line-height: 1.38; margin-bottom: 10px; }
  .treatments {
    position: absolute; left: 0; right: 0; bottom: 0; height: 230px;
    background: var(--charcoal);
    padding: 32px 34px 0 34px;
    color: var(--light-text);
  }
  .treatment { margin-bottom: 14px; }
  .treatment .section-title { font-size: 22px; margin-bottom: 6px; }
  .treatment .body-copy { margin-bottom: 0; font-size: 10px; }
</style>
</head>
<body>
  <main class="spread">
    <section class="page page--left">
      <div class="cost-panel">
        <h2 class="section-title">Breast<br>Reconstruction<br>and Cost</h2>
        <p class="body-copy">Navigating insurance policies can be daunting and stressful, so our staff is devoted to ensuring that our patients are secure and informed about their options and that their medical team is advocating on their behalf.</p>
        <p class="body-copy">Because of legislation passed in 1998, insurance companies must cover breast reconstruction following mastectomy. By law a woman is entitled to reconstructed breasts, breast symmetry and any future surgery needed to revise the primary reconstruction.</p>
        <p class="body-copy">We work to ensure our patients completely understand their right to coverage as well as the financial implications of any decisions they choose to make. We want to make sure that breast reconstruction is affordable and accessible to all women.</p>
        <span class="ribbon-mark" role="img" aria-label="Small pink awareness ribbon"></span>
      </div>
      <div class="ribbon-visual" role="img" aria-label="Photograph of a pink breast cancer awareness ribbon on white"></div>
      <p class="web-address">www.whitcombeplasticsurgery.com</p>
    </section>

    <section class="page page--right">
      <div class="portrait" role="img" aria-label="Portrait photograph showing a woman's face before and after facelift"></div>
      <article class="facelift">
        <h2 class="section-title">Face lift</h2>
        <p class="body-copy">Different people age at different rates depending on their genetic makeup and level of sun exposure in their youth. The time to look into your surgical options is when you feel that there are aspects of your facial appearance that you would like to improve.</p>
        <p class="body-copy">Often, it is when your exterior does not reflect your internal youth and vitality. There are different techniques with facelift surgery and these can be tailored to meet the needs of each patient; from a “mini” facelift for a patient in their 40s to a more extensive operation for a patient in their 70s.</p>
        <p class="body-copy">Dr. Whitcombe’s goal is to make you look refreshed but not different or “operated.”</p>
      </article>
      <div class="treatments">
        <article class="treatment">
          <h2 class="section-title">Neurolax</h2>
          <p class="body-copy">This product is a quick pick me up. Neurolax can help to improve a patient’s appearance, soften “frown” lines and elevate drooping brows all in the course of a two minute treatment.</p>
        </article>
        <article class="treatment">
          <h2 class="section-title">Facial fillers</h2>
          <p class="body-copy">Dr. Whitcombe uses fillers to target different aging areas of the face. It is often called the lunch time face lift. These products are great for plumping thin lips, softening smile lines, filling facial wrinkles or enhancing cheeks.</p>
        </article>
      </div>
    </section>
  </main>
</body>
</html>
```